Business Card Design

Professional solutions in (servers, security, networks, programming)

Industry/Entity Type

Business

Contact Information for Business Card

Tarek Hounayni
Cloud hosting services and systems support
DPV - RTLK - RTLB
netcare@qo-lam.com / 05917406238
www.qo-lam.com

```html
<!DOCTYPE html>
<html lang="en">
<head>
<meta charset="utf-8">
<title>Tarek Hounayni – Business Card</title>
<link rel="stylesheet" href="https://fonts.googleapis.com/css2?family=Montserrat:wght@500;600;700&display=swap">
<style>
  :root {
    --forest: #004c3c;
    --forest-deep: #003a2d;
    --lime: #8dc63f;
    --mist: #ebebeb;
    --paper: #f7f7f7;
    --teal: #137a62;
    --navy: #0e3a4c;
    --white: #ffffff;
  }
  * { margin: 0; padding: 0; box-sizing: border-box; }
  html, body {
    width: 1200px; height: 668px; overflow: hidden;
    background: var(--paper);
  }
  .card {
    position: relative; width: 1200px; height: 668px; overflow: hidden;
    background: var(--paper);
    font-family: "Montserrat", Arial, sans-serif;
  }
  .card__bands { position: absolute; inset: 0; width: 1200px; height: 668px; }
  .band--forest { fill: var(--forest); }
  .band--deep { fill: var(--forest-deep); }
  .band--lime { fill: var(--lime); }
  .band--mist { fill: var(--mist); }

  .identity { position: absolute; left: 21px; top: 102px; }
  .identity__name {
    color: var(--white); font-weight: 600; font-size: 49px;
    letter-spacing: 0; line-height: 1; text-transform: uppercase;
  }
  .identity__role {
    margin-top: 14px; color: var(--lime); font-weight: 600;
    font-size: 30px; line-height: 36px; text-transform: uppercase;
  }

  .contact {
    position: absolute; left: 735px; display: flex; align-items: center;
  }
  .contact__icon {
    width: 78px; height: 78px; border-radius: 50%;
    display: flex; align-items: center; justify-content: center;
    background: var(--teal); flex: none;
  }
  .contact__icon--lime { background: var(--lime); }
  .contact__icon svg { width: 40px; height: 40px; }
  .contact__text {
    margin-left: 27px; color: var(--navy); font-weight: 600;
    font-size: 22px; letter-spacing: 0.5px; text-transform: uppercase;
  }
  .contact__text--phone { font-size: 36px; font-weight: 700; letter-spacing: 1px; margin-left: 23px; }
  .contact--email { top: 247px; }
  .contact--phone { top: 393px; }
  .contact--web { top: 540px; }
</style>
</head>
<body>
<div class="card">
  <svg class="card__bands" viewBox="0 0 1200 668" aria-hidden="true">
    <polygon class="band--mist" points="765,0 848,0 585,668 495,668"/>
    <polygon class="band--lime" points="637,0 765,0 495,668 393,668"/>
    <polygon class="band--deep" points="565,0 637,0 393,668 368,668"/>
    <polygon class="band--forest" points="0,0 570,0 368,668 0,668"/>
  </svg>

  <div class="identity">
    <h1 class="identity__name">Tarek Hounayni</h1>
    <p class="identity__role">Cloud hosting services<br>and systems support<br>DPV - RTLK - RTLB</p>
  </div>

  <div class="contact contact--email">
    <span class="contact__icon">
      <svg viewBox="0 0 40 40" aria-hidden="true">
        <rect x="4" y="9" width="32" height="22" fill="#fff"/>
        <polyline points="4,9 20,22 36,9" fill="none" stroke="#137a62" stroke-width="2"/>
        <line x1="4" y1="31" x2="16" y2="19" stroke="#137a62" stroke-width="1.6"/>
        <line x1="36" y1="31" x2="24" y2="19" stroke="#137a62" stroke-width="1.6"/>
      </svg>
    </span>
    <span class="contact__text">netcare@qo-lam.com</span>
  </div>

  <div class="contact contact--phone">
    <span class="contact__icon contact__icon--lime">
      <svg viewBox="0 0 24 24" aria-hidden="true">
        <path fill="#fff" d="M6.6 10.8a15.1 15.1 0 0 0 6.6 6.6l2.2-2.2c.3-.3.7-.4 1-.2 1.1.4 2.3.6 3.6.6.6 0 1 .4 1 1V20c0 .6-.4 1-1 1A17 17 0 0 1 3 4c0-.6.4-1 1-1h3.5c.6 0 1 .4 1 1 0 1.3.2 2.5.6 3.6.1.3 0 .7-.2 1z"/>
      </svg>
    </span>
    <span class="contact__text contact__text--phone">05917406238</span>
  </div>

  <div class="contact contact--web">
    <span class="contact__icon">
      <svg viewBox="0 0 40 40" aria-hidden="true">
        <circle cx="20" cy="20" r="15" fill="#fff"/>
        <path fill="#137a62" d="M12 11c3 1 5 3 4 6s-4 2-5 5 1 5-1 6c-3-2-5-6-5-8 0-4 3-7 7-9zM24 8c3 1 6 3 8 6-2 0-4 1-5 3s1 4 0 6-3 1-4 4-1 5-3 6c-1-3 0-6-1-8s-3-3-2-6 4-2 5-5-1-4 2-6z"/>
      </svg>
    </span>
    <span class="contact__text">www.qo-lam.com</span>
  </div>
</div>
</body>
</html>
```